Website for "Bright Over Dusk Ltd" cleaning bsuiness

We require a website to expose our business to the local market. We want to provide background on who we are and what we do but in an easily digestible way. We clean domestic and commercial premises and want to provide a list of all of our services to potential customers. We operate out of Warrington in the UK.

We would like the website to be animated in some way so that the experience of using it is not dull or mundane. This website needs to be an extension of our company.

Target Market(s)

30 - 60 year olds for Domestic plus commercial clients

Industry/Entity Type

Cleaning Service

Coding

Coded - Design and coding required

Number of Pages Required

4 page

Font styles to use
Sans Serif

Colors
0455a3
3176b5
85acd3
cfdeed
ffffff
000000
1b1b1b
c8c8c8
757575

Requirements
Must have
• Logo which has been provided. Theme based around the logo and its colours. Simple layout to avoid confusion.
Nice to have
• Animations where possible to impress the customer.
Should not have
• any pictures of cleaning equipment, fairies, maids etc

```html
<!DOCTYPE html>
<html lang="en">
<head>
<meta charset="utf-8">
<title>Bright Over Dusk Ltd – Professional Cleaning Service</title>
<link href="https://fonts.googleapis.com/css2?family=Open+Sans:wght@400;600;700;800&display=swap" rel="stylesheet">
<style>
  :root {
    --brand-blue: #0455a3;
    --mid-blue: #3176b5;
    --soft-blue: #85acd3;
    --pale-blue: #cfdeed;
    --bright-blue: #1a8ce6;
    --card-blue: #2a6cc0;
    --card-arrow: #1f7be0;
    --panel-blue: #26568a;
    --navy: #0c1c33;
    --white: #ffffff;
    --ink: #1b1b1b;
    --grey-line: #c8c8c8;
    --grey-text: #757575;
    --page-bg: #f2f2f2;
  }
  * { box-sizing: border-box; margin: 0; padding: 0; }
  html, body { width: 1120px; height: 1200px; overflow: hidden; }
  body {
    font-family: "Open Sans", sans-serif;
    background: var(--page-bg);
    color: var(--ink);
    position: relative;
  }

  /* Header */
  .brand-card {
    position: absolute; left: 92px; top: 0; width: 214px; height: 180px;
    background: var(--white);
    box-shadow: 0 2px 6px rgba(0,0,0,.12);
    display: flex; align-items: center; justify-content: center; gap: 10px;
    padding: 0 16px; z-index: 3;
  }
  .brand-mark { width: 16px; height: 16px; background: var(--brand-blue); flex: none; }
  .brand-name {
    font-size: 22px; font-weight: 700; color: var(--brand-blue); line-height: 1.15;
  }
  .contact-bar {
    position: absolute; top: 24px; left: 666px;
    display: flex; align-items: center; gap: 8px;
    font-size: 20px; color: #333;
  }
  .contact-bar svg { width: 22px; height: 22px; }
  .social-links {
    position: absolute; top: 26px; left: 914px; display: flex; gap: 3px;
  }
  .social-links span { width: 26px; height: 26px; display: block; }
  .social-links .s1 { background: #3b5a9a; }
  .social-links .s2 { background: #41a9e6; }
  .social-links .s3 { background: #1c7bb7; }
  .social-links .s4 { background: #dd4b39; }
  .main-nav {
    position: absolute; top: 76px; right: 92px;
    display: flex; font-size: 14px; font-weight: 700;
  }
  .main-nav a {
    text-decoration: none; color: #333; padding: 0 16px;
    border-left: 1px solid var(--grey-line); line-height: 18px;
  }
  .main-nav a:first-child { border-left: 0; color: var(--bright-blue); }
  .main-nav a:last-child { padding-right: 0; }

  /* Hero slider */
  .hero {
    position: absolute; left: 92px; top: 106px; width: 936px; height: 396px;
    background: var(--white); padding: 7px;
  }
  .hero-photo {
    position: absolute; left: 7px; top: 7px; width: 633px; height: 382px;
    background: linear-gradient(135deg, #e8e3dc 0%, #f4f4f2 45%, #b9cfe0 70%, #eeeeee 100%);
  }
  .hero-panel {
    position: absolute; left: 640px; top: 7px; width: 290px; height: 382px;
    background: var(--panel-blue); color: var(--white); padding: 92px 0 0 38px;
  }
  .hero-panel h1 { font-size: 34px; font-weight: 800; line-height: 36px; letter-spacing: .5px; }
  .hero-panel h2 { font-size: 27px; font-weight: 400; line-height: 32px; }
  .hero-panel p { font-size: 13px; line-height: 20px; margin: 10px 0 0 3px; width: 200px; }
  .btn-read {
    display: inline-block; margin: 14px 0 0 3px; width: 136px; height: 38px;
    background: var(--bright-blue); color: var(--white); text-decoration: none;
    text-align: center; line-height: 38px; font-size: 14px; font-weight: 600;
  }
  .slider-arrows { position: absolute; right: 17px; bottom: 15px; display: flex; gap: 3px; }
  .slider-arrows svg { width: 16px; height: 16px; }

  /* Services */
  .services {
    position: absolute; left: 0; top: 542px; width: 1120px; height: 658px;
    background: linear-gradient(180deg, #0b1a30 0%, #13263f 22%, #2a3446 55%, #3a3f48 100%);
  }
  .services-bg {
    position: absolute; inset: 120px 0 0 0;
    background: radial-gradient(ellipse at 30% 40%, rgba(90,100,110,.35), transparent 60%),
                radial-gradient(ellipse at 80% 70%, rgba(20,30,45,.45), transparent 60%);
  }
  .services h2 {
    position: absolute; top: 28px; width: 100%; text-align: center;
    font-size: 38px; font-weight: 700; color: var(--white);
  }
  .service-tabs { position: absolute; top: 90px; left: 333px; display: flex; }
  .service-tabs a {
    display: block; height: 34px; line-height: 34px; text-align: center;
    font-size: 14px; text-decoration: none; position: relative;
  }
  .tab-active { width: 216px; background: var(--bright-blue); color: var(--white); }
  .tab-active::after {
    content: ""; position: absolute; left: 50%; bottom: -5px; margin-left: -5px;
    border: 5px solid transparent; border-bottom: 0; border-top-color: var(--bright-blue);
  }
  .tab-idle { width: 239px; background: #ebebeb; color: var(--brand-blue); }

  .service-grid {
    position: absolute; top: 172px; left: 103px;
    display: grid; grid-template-columns: repeat(3, 278px); column-gap: 42px; row-gap: 44px;
  }
  .service-card { width: 278px; height: 190px; }
  .service-photo { height: 141px; }
  .service-bar {
    height: 49px; display: flex; background: var(--card-blue); color: var(--white);
  }
  .service-bar span {
    flex: 1; display: flex; align-items: center; padding: 0 8px 0 18px;
    font-size: 14px; font-weight: 600; line-height: 18px;
  }
  .service-bar i {
    width: 42px; background: var(--card-arrow);
    display: flex; align-items: center; justify-content: center;
  }
  .service-bar svg { width: 12px; height: 14px; }
  .p1 { background: linear-gradient(120deg, #dfe6ea, #f0c6c8 55%, #c8242a); }
  .p2 { background: linear-gradient(180deg, #9aa0a8, #dcdcdc 60%, #cfcfcf); }
  .p3 { background: linear-gradient(120deg, #c79a88, #3b5f8e 50%, #8f7560); }
  .p4 { background: linear-gradient(135deg, #b5bcc2, #dfe3e6 50%, #9ea6ad); }
  .p5 { background: linear-gradient(135deg, #eef0ee, #e2ddd2 60%, #f3f3f1); }
  .p6 { background: linear-gradient(135deg, #9fc3e4, #d8e6f1 50%, #e2c05c); }
</style>
</head>
<body>
  <header>
    <div class="brand-card">
      <span class="brand-mark"></span>
      <span class="brand-name">Bright Over Dusk Ltd</span>
    </div>
    <div class="contact-bar">
      <svg viewBox="0 0 24 24" fill="none" stroke="#8a8a8a" stroke-width="1.4"><path d="M5 3l4 1 1 5-2 1c1 3 3 5 6 6l1-2 5 1 1 4c-1 2-3 2-5 2C9 20 4 15 3 8c0-2 0-4 2-5z"/></svg>
      <span>0012 - 4830 - 0917</span>
    </div>
    <div class="social-links" aria-label="Social links">
      <span class="s1"></span><span class="s2"></span><span class="s3"></span><span class="s4"></span>
    </div>
    <nav class="main-nav">
      <a href="#">Home</a><a href="#">About Us</a><a href="#">Services</a><a href="#">Contact Us</a>
    </nav>
  </header>

  <section class="hero">
    <div class="hero-photo" role="img" aria-label="Photo of a bright bedroom being tidied"></div>
    <div class="hero-panel">
      <h1>CLEANING</h1>
      <h2>SERVICES</h2>
      <p>Donec dapibus at nunc eget luctus. Praesent eu mattis enim, et commodo sapien. Aliquam posuere justo.</p>
      <a class="btn-read" href="#">Read More</a>
    </div>
    <div class="slider-arrows">
      <svg viewBox="0 0 16 16"><circle cx="8" cy="8" r="8" fill="#e6e6e6"/><path d="M9.5 5L6.5 8l3 3" stroke="#444" stroke-width="1.6" fill="none"/></svg>
      <svg viewBox="0 0 16 16"><circle cx="8" cy="8" r="8" fill="#e6e6e6"/><path d="M6.5 5l3 3-3 3" stroke="#444" stroke-width="1.6" fill="none"/></svg>
    </div>
  </section>

  <section class="services">
    <div class="services-bg" role="img" aria-label="Soft blurred background photo"></div>
    <h2>Our Services</h2>
    <div class="service-tabs">
      <a class="tab-active" href="#">Domestic Service</a>
      <a class="tab-idle" href="#">Commercial Cleaning</a>
    </div>
    <div class="service-grid">
      <article class="service-card">
        <div class="service-photo p1" role="img" aria-label="Photo of window cleaning at home"></div>
        <div class="service-bar"><span>Weekly, fotnightly, monthly and adhoc cleans available</span><i><svg viewBox="0 0 12 14"><path d="M3 1l6 6-6 6" stroke="#fff" stroke-width="2" fill="none"/></svg></i></div>
      </article>
      <article class="service-card">
        <div class="service-photo p2" role="img" aria-label="Photo of a carpet being cleaned"></div>
        <div class="service-bar"><span>Carpet Cleaning</span><i><svg viewBox="0 0 12 14"><path d="M3 1l6 6-6 6" stroke="#fff" stroke-width="2" fill="none"/></svg></i></div>
      </article>
      <article class="service-card">
        <div class="service-photo p3" role="img" aria-label="Photo of a shirt being ironed"></div>
        <div class="service-bar"><span>Ironing</span><i><svg viewBox="0 0 12 14"><path d="M3 1l6 6-6 6" stroke="#fff" stroke-width="2" fill="none"/></svg></i></div>
      </article>
      <article class="service-card">
        <div class="service-photo p4" role="img" aria-label="Photo of tiled bathroom steam cleaning"></div>
        <div class="service-bar"><span>Tiled floor steam clean</span><i><svg viewBox="0 0 12 14"><path d="M3 1l6 6-6 6" stroke="#fff" stroke-width="2" fill="none"/></svg></i></div>
      </article>
      <article class="service-card">
        <div class="service-photo p5" role="img" aria-label="Photo of a living room being vacuumed"></div>
        <div class="service-bar"><span>End of tenancy clean</span><i><svg viewBox="0 0 12 14"><path d="M3 1l6 6-6 6" stroke="#fff" stroke-width="2" fill="none"/></svg></i></div>
      </article>
      <article class="service-card">
        <div class="service-photo p6" role="img" aria-label="Photo of windows in a new house being wiped"></div>
        <div class="service-bar"><span>New house pre moving in clean</span><i><svg viewBox="0 0 12 14"><path d="M3 1l6 6-6 6" stroke="#fff" stroke-width="2" fill="none"/></svg></i></div>
      </article>
    </div>
  </section>
</body>
</html>
```